Equipment Finance Specialist I work with companies who need the funds to buy their equipment

I would like a business card that stands out on the shelves. I want to be able to hand it to someone and say WOW. This card should have my logo.
You can put color into it I am very open on design and color

What my company does is we deal with dealerships that sell equipment such as Dump Trucks garbage trucks tractors trailers. Customers get referred to us and depending on their time in business we will ask for the following items

Companies that have been in business for more than two years we have a credit application program up to 250K . With this program we need the following items Credit application filled out(which is what I would like to be able for the customer to click on my website to get.) as well as three current month bank statements.

Deals over 250k we will need the following items

2 years business tax returns
2 years personal tax returns
Profit & Loss statement
Personal Financial Statement

what we do
100% FINANCING
SEASONAL PAYMENTS
LOAN BALLOON PAYMENTS
TRAC LEASING
LOW-INTEREST REFINANCING RATES
DEBT CONSOLIDATION

We specialize in creative financing solutions and offer a variety of reliable, flexible and expandable lending choices.

Target Market(s)

Trucking Companies

Industry/Entity Type

Trucking Company

Contact Information for Business Card

* $250,000 Application only Program
* Loans from $30,000 to 5,000,000
* Competitive Interest Rates

Font styles to use
Serif
Sans Serif

Colors

Designer to choose colors to be used in the design.

Requirements
Must have
• On the back of the card.
• * $250,000 Application only Program
• * Loans from $30,000 to 5,000,000
• My name, email, website. address
• * Competitive Interest Rates
• * 100% Financing
Nice to have
• I want my logo to pop on the card
• My logo is the great one I would like to use
Should not have
• I am up for your creativity as well

```html
<!DOCTYPE html>
<html lang="en">
<head>
<meta charset="UTF-8">
<title>Ironhaul Finance – Business Card</title>
<link href="https://fonts.googleapis.com/css2?family=Open+Sans:ital,wght@0,400;0,600;0,700;0,800;1,700&display=swap" rel="stylesheet">
<style>
  :root{
    --navy:#0d2a78;
    --navy-deep:#0a2264;
    --red:#d5173a;
    --paper:#eef0f3;
    --ink:#1d2330;
    --rule:#b9c0cf;
    --steel-light:#e4e7ec;
    --steel-dark:#8f97a6;
    --bg:#3a3c40;
  }
  *{box-sizing:border-box;margin:0;padding:0}
  html,body{width:1200px;height:896px;overflow:hidden;background:var(--bg);font-family:"Open Sans",Arial,sans-serif}
  .sheet{width:1200px;height:896px;display:flex;flex-direction:column;align-items:center;justify-content:center;gap:20px}
  .card{position:relative;width:760px;height:420px;overflow:hidden;box-shadow:0 8px 24px rgba(0,0,0,.35)}
  .card svg.shapes{position:absolute;inset:0}

  /* FRONT */
  .front{background:var(--paper)}
  .front .decor{position:absolute;left:20px;top:10px;width:300px;height:200px;border-radius:40px;
    background:linear-gradient(135deg,rgba(200,205,214,.35),rgba(200,205,214,0))}
  .identity{position:absolute;left:44px;top:108px;color:var(--ink)}
  .identity .name{font-size:30px;font-weight:800;letter-spacing:1px;color:var(--navy);line-height:1}
  .identity .name span{color:var(--red)}
  .identity .role,.identity .addr{font-size:17px;line-height:1.3}
  .identity .role{margin-top:6px}
  .brand{position:absolute;left:450px;top:118px;display:flex;align-items:center;gap:12px}
  .brand .dot{width:60px;height:60px;border-radius:50%;background:var(--navy)}
  .brand .word{font-size:30px;font-weight:800;color:var(--navy);line-height:1;letter-spacing:1px}
  .divider{position:absolute;left:300px;top:212px;width:390px;height:1px;background:var(--rule)}
  .contacts{position:absolute;right:40px;top:224px;text-align:right;color:var(--ink);font-size:17px;line-height:1.5}
  .contacts li{list-style:none;display:flex;justify-content:flex-end;align-items:center;gap:8px}
  .contacts svg{width:14px;height:14px;fill:var(--navy)}
  .bullets{position:absolute;color:#fff;font-size:17px;line-height:1.45;list-style:none}
  .bullets li::before{content:"";display:inline-block;width:8px;height:8px;border-radius:50%;background:#fff;margin-right:9px;vertical-align:middle}
  .bullets.left{left:44px;top:262px}
  .bullets.right{right:40px;top:346px}

  /* BACK */
  .back{background:var(--navy)}
  .truck-art{position:absolute;left:70px;top:50px;width:230px;height:200px;border-radius:50%;
    background:radial-gradient(circle at 40% 40%,var(--steel-light),var(--steel-dark))}
  .services{position:absolute;left:460px;top:60px;color:#fff}
  .services h2{font-size:19px;font-weight:800;letter-spacing:.5px;margin-bottom:8px}
  .services ul{list-style:none;font-size:15px;line-height:1.55;text-transform:uppercase}
  .services li::before{content:"";display:inline-block;width:8px;height:8px;border-radius:50%;background:#fff;margin-right:9px;vertical-align:middle}
  .back .vrule{position:absolute;left:430px;top:60px;width:1px;height:190px;background:rgba(255,255,255,.35)}
  .requirements{position:absolute;left:0;right:0;top:290px;text-align:center;color:#fff;font-size:18px;line-height:1.45}
</style>
</head>
<body>
<main class="sheet">

  <section class="card front" aria-label="Card front">
    <div class="decor" role="img" aria-label="Faint truck decoration"></div>
    <svg class="shapes" width="760" height="420" viewBox="0 0 760 420" aria-hidden="true">
      <polygon points="0,250 400,250 440,336 760,336 760,420 0,420" fill="var(--navy)"/>
    </svg>
    <div class="identity">
      <p class="name">DANIEL <span>CARTER</span></p>
      <p class="role">Managing Director</p>
      <p class="addr">421, Address line here,<br>45452,Country Name</p>
    </div>
    <div class="brand">
      <div class="dot"></div>
      <div class="word">IRONHAUL<br>FINANCE</div>
    </div>
    <div class="divider"></div>
    <ul class="contacts">
      <li>044-555 010 234
        <svg viewBox="0 0 24 24"><path d="M6.6 10.8a15 15 0 006.6 6.6l2.2-2.2c.3-.3.7-.4 1-.2 1.1.4 2.3.6 3.6.6.6 0 1 .4 1 1V20c0 .6-.4 1-1 1A17 17 0 013 4c0-.6.4-1 1-1h3.5c.6 0 1 .4 1 1 0 1.3.2 2.5.6 3.6.1.3 0 .7-.2 1z"/></svg></li>
      <li>info@ironhaulmail.com
        <svg viewBox="0 0 24 24"><path d="M2 5h20v14H2z M2 5l10 8 10-8" stroke="#fff" stroke-width="1.5"/></svg></li>
      <li>www.ironhaulfinance.com
        <svg viewBox="0 0 24 24"><circle cx="12" cy="12" r="10"/></svg></li>
    </ul>
    <ul class="bullets left">
      <li>$250,000 Application only Program</li>
      <li>Loans from $30,000 to 5,000,000</li>
    </ul>
    <ul class="bullets right">
      <li>Competitive Interest Rates</li>
      <li>100% Financing</li>
    </ul>
  </section>

  <section class="card back" aria-label="Card back">
    <svg class="shapes" width="760" height="420" viewBox="0 0 760 420" aria-hidden="true">
      <rect x="0" y="275" width="760" height="90" fill="var(--red)"/>
    </svg>
    <div class="truck-art" role="img" aria-label="Silver truck illustration in a circle"></div>
    <div class="vrule"></div>
    <div class="services">
      <h2>WHAT WE DO</h2>
      <ul>
        <li>100% Financing</li>
        <li>Seasonal Payments</li>
        <li>Loan Balloon Payments</li>
        <li>TRAC Leasing</li>
        <li>Low-Interest Refinancing Rates</li>
        <li>Debt Consolidation</li>
      </ul>
    </div>
    <p class="requirements">2 years business tax returns | 2 years personal tax returns<br>Profit &amp; Loss statement | Personal Financial Statement</p>
  </section>

</main>
</body>
</html>
```